Cedar Hall businesscard

We changed our name and logo, now we need new business cards.
3-4/72 Marlow Street Wrenfield 2196
www.cedarhall-example.org.au
info@cedarhall-example.org.au
Lorna-Jean Whitcombe
Senior Pastor
ph: 02 95874210

```html
<!DOCTYPE html>
<html lang="en">
<head>
<meta charset="utf-8">
<title>Cedar Hall business card</title>
<link rel="stylesheet" href="https://fonts.googleapis.com/css2?family=Mulish:wght@300;400;700&display=swap">
<style>
  :root {
    --page: #e9ebed;
    --card: #f7f8f9;
    --card-edge: #c9cfd5;
    --slate: #4e6577;
    --slate-dark: #3a4b5a;
    --name-light: #e2e6ea;
    --title-light: #d0d6dc;
  }
  * { box-sizing: border-box; margin: 0; padding: 0; }
  html, body {
    width: 1200px; height: 970px; overflow: hidden;
    background: var(--page);
    font-family: "Mulish", sans-serif;
  }
  .business-card {
    position: absolute; left: 100px; top: 205px;
    width: 1000px; height: 560px;
    background: var(--card);
    border: 1.5px solid var(--card-edge);
    border-radius: 30px;
    overflow: hidden;
    box-shadow: 0 18px 40px rgba(40, 55, 70, 0.12);
  }
  .feature-circle {
    position: absolute;
    left: -283px; top: -80px;
    width: 720px; height: 720px;
    border-radius: 50%;
    background: var(--slate);
    opacity: 0.88;
    box-shadow: inset 0 0 0 6px rgba(255,255,255,0.12);
  }
  .person {
    position: absolute; left: 44px; top: 246px;
  }
  .person-name {
    font-weight: 700; font-size: 25px; color: var(--name-light);
    letter-spacing: 0.3px;
  }
  .person-title {
    font-weight: 400; font-size: 22px; color: var(--title-light);
    margin-top: 4px;
  }
  .brand {
    position: absolute; left: 660px; top: 150px;
    display: flex; align-items: center; gap: 16px;
  }
  .brand-dot {
    width: 22px; height: 22px; border-radius: 50%;
    background: var(--slate);
  }
  .brand-name {
    font-weight: 300; font-size: 50px; color: var(--slate-dark);
    letter-spacing: 1px;
  }
  .divider {
    position: absolute; left: 463px; right: 0; top: 354px;
    height: 2px; background: var(--slate-dark);
  }
  .contact-list {
    position: absolute; right: 32px; top: 384px;
    list-style: none; text-align: right;
    font-size: 24px; color: var(--slate-dark);
  }
  .contact-list li {
    display: flex; justify-content: flex-end; align-items: center; gap: 8px;
    height: 32px;
  }
  .contact-list li.address { margin-top: 15px; }
  .contact-icon { width: 22px; height: 22px; fill: var(--slate-dark); flex: none; }
</style>
</head>
<body>
  <section class="business-card">
    <div class="feature-circle"></div>
    <div class="person">
      <p class="person-name">Lorna-Jean Whitcombe</p>
      <p class="person-title">Senior Pastor</p>
    </div>
    <div class="brand">
      <span class="brand-dot"></span>
      <span class="brand-name">Cedar Hall</span>
    </div>
    <div class="divider"></div>
    <ul class="contact-list">
      <li>02 95874210
        <svg class="contact-icon" viewBox="0 0 24 24" aria-hidden="true"><path d="M3 9c0-3 4-5 9-5s9 2 9 5v2h-5V9H8v2H3zM7 12h10l3 7H4z"/><circle cx="12" cy="15.5" r="2" fill="#f7f8f9"/></svg>
      </li>
      <li>info@cedarhall-example.org.au
        <svg class="contact-icon" viewBox="0 0 24 24" aria-hidden="true"><path d="M2 5h20v14H2z"/><path d="M3 6l9 7 9-7" fill="none" stroke="#f7f8f9" stroke-width="1.6"/></svg>
      </li>
      <li>www.cedarhall-example.org.au
        <svg class="contact-icon" viewBox="0 0 24 24" aria-hidden="true"><circle cx="12" cy="12" r="10"/><g fill="none" stroke="#f7f8f9" stroke-width="1.3"><ellipse cx="12" cy="12" rx="4" ry="10"/><path d="M2 12h20M4 7h16M4 17h16"/></g></svg>
      </li>
      <li class="address">3-4/72 Marlow Street Wrenfield 2196
        <svg class="contact-icon" viewBox="0 0 24 24" aria-hidden="true"><path d="M12 2l11 10h-3v10h-6v-6h-4v6H4V12H1z"/></svg>
      </li>
    </ul>
  </section>
</body>
</html>
```